Infographics for nature conservation project / Infografiken für ein Naturschutzprojekt
Zielgruppe
Harrow Wildlife Trust (HWT) is an international conservation organisation based in Germany that has been implementing conservation projects in outstanding natural places in Africa, South America, South-East Asia, and Europe for decades. The HWT Continental Initiative safeguards large, biodiverse wilderness areas, mainly in Eastern Europe.
Since this year, a 5-year project (www.openmarshland.org), kicked-off to save the landscape of Belarusian and Ukrainian Polesia. Therefore, a consortium of nature conservation organisations from 4 different countries joined forces to protect this natural landscape:
• KRN-WingWatch Belarus
• DOTM-WingWatch Ukraine
• Caledon Society for Avian Study
• Harrow Wildlife Trust https://hwt-nature.org/en/projects/polesia-europes-largest-wilderness-area/
Polesia is one of the biggest and most impressive wilderness areas in Europe. It spans over 180,000 square kilometres and stretches across the boundaries of Poland, Belarus, Ukraine and Russia. With its naturally meandering river, gigantic mires, wetlands and floodplain forests, Polesia is a treasure for birds, amphibians and many other animal and plant species. It is not only key to wildlife, but also to human beings by providing reams of vital benefits as e.g. contributing to a country’s economy, regulating climate, providing clean water, storing carbon, supporting human health and many more.
Here (https://hwt-nature.org/en/news/amazonia-europe/) you will find a description and some pictures of the area and the website (www.openmarshland.org) on which the infographics will be presented..
The target group is the donor, but also media, local political decision makers, and the international conservation community will visit the website.
Aufgabenstellung
The designer should create six (6) infographics. The infographics will be used on the project website www.openmarshland.org to give a short and comprehensive introduction to the project.
The designer is free to choose, whether all infographics will be created as stand alone graphics or interconnected in one single file (examples below). This is up to the designers creativity and ideas, we are open for both suggestions.
If the designer choses the latter, having both a landscape- and a portrait- layout version for the different layouts of the website on a desktop and smartphone would be preferred (not mandatory).
The infographics will need to be incorporated into the website ideally by Friday,8th of May.
The six infographics needed should resemble, respectively, the:
1. General project facts: Project duration 2019-2023 (5 years), Partnership of 4 NGOs, Project area and size: 5.8 mio ha (located along Belarusian-Ukrainian border)
2. Project outcome 1: Biodiversity is better protected through the expansion by at least 100,000 ha, improved financing and international recognition of the protected area network in the core project area --> Expansion of protected areas by 100,000 hectare
3. Project outcome 2: Improved management and on-site protection in the protected and interconnected core area of over 1 Mio ha --> Improvement of protected areas management in over 1 million hectare
4. Project outcome 3: Mires and wetlands (6,000 ha) rewetted --> Restoration of 6,000 hectares of drained mires
5. Project outcome 4: Awareness and knowledge in relation to Polesia increased among the local population which leads to active support towards the conservation of key areas --> Increase of awareness and knowledge
6. Project outcome 5: Development of alternative livelihoods based on sustainable use of nature. In this way, nature-based jobs will be created which will replace other harmful practices in the area. --> Development of al..

```html
<!DOCTYPE html>
<html lang="en">
<head>
<meta charset="utf-8">
<title>General Project Facts</title>
<link href="https://fonts.googleapis.com/css2?family=Exo+2:wght@300;400&family=Open+Sans:wght@300;700&family=Oswald:wght@500&family=Saira+Condensed:wght@400&display=swap" rel="stylesheet">
<style>
  :root {
    --navy: #1b3f80;
    --green: #8cac4f;
    --green-light: #a9c578;
    --panel: #dce2e6;
    --dots: #b5c1c8;
    --bg: #f7f7f7;
  }
  * { margin: 0; padding: 0; box-sizing: border-box; }
  html, body { width: 768px; height: 1200px; overflow: hidden; }
  body {
    background: radial-gradient(circle at 50% 48%, #ffffff 0%, var(--bg) 60%, #f3f3f3 100%);
    font-family: "Exo 2", sans-serif;
    position: relative;
  }
  .facts { position: absolute; top: 78px; text-align: center; }
  .fact-value { font-weight: 300; color: var(--green); font-size: 26px; line-height: 1; }
  .fact-value small { font-size: 18px; }
  .fact-label { font-weight: 300; color: var(--navy); font-size: 15px; line-height: 19px; }
  .fact-duration { left: 20px; width: 110px; }
  .fact-partners { left: 160px; width: 115px; }
  .fact-area { left: 285px; width: 145px; }
  .icon-box { display: block; margin: 0 auto; }

  .duration-mark { position: relative; width: 110px; height: 126px; }
  .duration-num { position: absolute; left: 24px; top: -4px; font-weight: 300; font-size: 50px; line-height: 1; color: var(--green); z-index: 1; }
  .duration-unit { position: absolute; left: 56px; top: 0; font-weight: 300; font-size: 14px; line-height: 1; color: var(--green); }
  .duration-art {
    position: absolute; left: 7px; top: 22px; width: 96px; height: 96px; border-radius: 50%;
    background: radial-gradient(circle, var(--navy) 0 30%, #f7f7f7 31% 60%, var(--green) 61% 100%);
    opacity: 0.9;
  }

  .title { position: absolute; right: 24px; top: 76px; text-align: right; font-family: "Open Sans", sans-serif; }
  .title-top { font-size: 34px; color: var(--navy); line-height: 1; letter-spacing: 0.5px; }
  .title-top b { font-weight: 700; }
  .title-top span { font-weight: 300; }
  .title-rule { display: block; margin: 6px 0 4px auto; width: 270px; height: 6px; }
  .title-bottom { font-size: 34px; font-weight: 700; color: var(--green); line-height: 1; }

  .outcome { position: absolute; left: 24px; width: 720px; height: 80px; }
  .outcome-num {
    position: absolute; left: 0; top: 0; width: 40px; height: 80px;
    font-family: "Oswald", sans-serif; font-weight: 500; color: #fff; font-size: 44px;
    display: flex; align-items: center; justify-content: center;
  }
  .outcome-text {
    position: absolute; left: 40px; top: 0; width: 258px; height: 80px; background: var(--panel);
    display: flex; align-items: center; justify-content: flex-end; padding-right: 23px;
    text-align: right; font-family: "Saira Condensed", sans-serif; font-size: 15px; line-height: 18px;
  }
  .outcome-text::after {
    content: ""; position: absolute; right: -10px; top: 40px; transform: translateY(-50%);
    border-left: 10px solid var(--panel); border-top: 10px solid transparent; border-bottom: 10px solid transparent;
  }
  .is-navy .outcome-num { background: var(--navy); }
  .is-navy .outcome-text { color: var(--navy); }
  .is-green .outcome-num { background: var(--green); }
  .is-green .outcome-text { color: var(--green); }
  .outcome-dots { position: absolute; left: 346px; top: 37px; width: 234px; height: 6px; }
  .outcome-icon { position: absolute; border-radius: 6px; }
  .icon-navy { background: linear-gradient(135deg, #2d5396, var(--navy)); }
  .icon-green { background: linear-gradient(135deg, var(--green-light), var(--green)); }

  .emblem {
    position: absolute; left: 282px; top: 917px; width: 206px; height: 206px; border-radius: 50%;
    background: #fff; box-shadow: 0 4px 14px rgba(0,0,0,0.08);
    display: flex; align-items: center; justify-content: center;
  }
  .emblem-name { font-family: "Open Sans", sans-serif; font-weight: 700; color: var(--navy); font-size: 22px; text-align: center; line-height: 1.1; }
</style>
</head>
<body>
  <section class="facts fact-duration">
    <div class="duration-mark icon-box">
      <div class="duration-art" role="img" aria-label="Clock with circular arrows showing five years"></div>
      <span class="duration-num">5</span>
      <span class="duration-unit">years</span>
    </div>
    <p class="fact-label">Project duration<br>2019-2023</p>
  </section>

  <section class="facts fact-partners">
    <p class="fact-value">4 NGOs</p>
    <div class="icon-box" role="img" aria-label="Two shaking hands in navy and green" style="width:112px;height:74px;margin-top:14px;margin-bottom:10px;background:linear-gradient(135deg,#1b3f80 45%,#8cac4f 55%);border-radius:24px;"></div>
    <p class="fact-label">Partnership</p>
  </section>

  <section class="facts fact-area">
    <p class="fact-value">5.8 <small>mio ha</small></p>
    <svg class="icon-box" width="110" height="92" viewBox="0 0 110 92" style="margin-top:6px">
      <line x1="8" y1="6" x2="8" y2="62" stroke="#8cac4f" stroke-width="4"/>
      <polygon points="8,0 0,10 16,10" fill="#8cac4f"/>
      <polygon points="8,68 0,58 16,58" fill="#8cac4f"/>
      <line x1="30" y1="80" x2="84" y2="80" stroke="#8cac4f" stroke-width="4"/>
      <polygon points="24,80 34,72 34,88" fill="#8cac4f"/>
      <polygon points="90,80 80,72 80,88" fill="#8cac4f"/>
      <foreignObject x="20" y="0" width="80" height="64">
        <div xmlns="http://www.w3.org/1999/xhtml" role="img" aria-label="Folded map of the project region" style="width:80px;height:64px;background:linear-gradient(160deg,#9dc25c,#8cac4f 55%,#1b3f80);"></div>
      </foreignObject>
    </svg>
    <p class="fact-label">located along<br>Belarusian-Ukrainian<br>border</p>
  </section>

  <header class="title">
    <h1 class="title-top"><b>GENERAL</b> <span>PROJECT</span></h1>
    <svg class="title-rule" viewBox="0 0 270 6"><line x1="3" y1="3" x2="268" y2="3" stroke="#b5c1c8" stroke-width="5" stroke-linecap="round" stroke-dasharray="8 16"/></svg>
    <h2 class="title-bottom">FACTS</h2>
  </header>

  <article class="outcome is-navy" style="top:313px">
    <div class="outcome-num">1</div>
    <p class="outcome-text">EXPANSION OF PROTECTED AREAS<br>BY 100,000 HECTARE</p>
    <svg class="outcome-dots" viewBox="0 0 234 6"><line x1="3" y1="3" x2="231" y2="3" stroke="#b5c1c8" stroke-width="5" stroke-linecap="round" stroke-dasharray="6 14"/></svg>
    <div class="outcome-icon icon-navy" role="img" aria-label="Outlined area with a location pin" style="left:623px;top:-7px;width:97px;height:94px;"></div>
  </article>

  <article class="outcome is-green" style="top:437px">
    <div class="outcome-num">2</div>
    <p class="outcome-text">IMPROVEMENT OF PROTECTED AREAS<br>MANAGEMENT IN OVER<br>1 MILLION HECTARE</p>
    <svg class="outcome-dots" viewBox="0 0 234 6"><line x1="3" y1="3" x2="231" y2="3" stroke="#b5c1c8" stroke-width="5" stroke-linecap="round" stroke-dasharray="6 14"/></svg>
    <div class="outcome-icon icon-green" role="img" aria-label="Outlined map with a location marker and binoculars" style="left:608px;top:-1px;width:112px;height:82px;"></div>
  </article>

  <article class="outcome is-navy" style="top:561px">
    <div class="outcome-num">3</div>
    <p class="outcome-text">RESTORATION OF 6,000 HECTARES<br>OF DRAINED MIRES</p>
    <svg class="outcome-dots" viewBox="0 0 234 6"><line x1="3" y1="3" x2="231" y2="3" stroke="#b5c1c8" stroke-width="5" stroke-linecap="round" stroke-dasharray="6 14"/></svg>
    <div class="outcome-icon" role="img" aria-label="Reeds and bulrushes growing from wet ground" style="left:616px;top:-6px;width:96px;height:93px;background:linear-gradient(180deg,#f7f7f7,#1b3f80);"></div>
  </article>

  <article class="outcome is-green" style="top:685px">
    <div class="outcome-num">4</div>
    <p class="outcome-text">INCREASE OF AWARENESS AND<br>KNOWLEDGE</p>
    <svg class="outcome-dots" viewBox="0 0 234 6"><line x1="3" y1="3" x2="231" y2="3" stroke="#b5c1c8" stroke-width="5" stroke-linecap="round" stroke-dasharray="6 14"/></svg>
    <div class="outcome-icon icon-green" role="img" aria-label="Speaker with a megaphone addressing a small crowd" style="left:616px;top:9px;width:96px;height:64px;"></div>
  </article>

  <article class="outcome is-navy" style="top:809px">
    <div class="outcome-num">5</div>
    <p class="outcome-text">DEVELOPMENT OF ALTERNATIVE<br>LIVELIHOODS</p>
    <svg class="outcome-dots" viewBox="0 0 234 6"><line x1="3" y1="3" x2="231" y2="3" stroke="#b5c1c8" stroke-width="5" stroke-linecap="round" stroke-dasharray="6 14"/></svg>
    <div class="outcome-icon icon-navy" role="img" aria-label="Three linked circles around a water drop, with care and farming symbols" style="left:616px;top:-4px;width:96px;height:90px;border-radius:45px;"></div>
  </article>

  <footer class="emblem">
    <p class="emblem-name">OPEN<br>MARSHLAND</p>
  </footer>
</body>
</html>
```